Website redesign

We've inherited a Tilecraft Website that we'd like to change to a Pagemill website to match our other sites.

Site I want redesigned is: https://www.corvellawings.com/
which will change to www.corvellaskytours.com.au

Our other websites I want it to match:
https://marloweskytours.com.au/
https://penfaricays.au/
https://tindaleskytours.com.au/
https://brightvalewings.com.au/

I do not want the design to deviate too much from the others, the main difference will be colours that need to align with the logo I've uploaded.

Pages I want:
Home
About Us
Gallery
News/Blog
Overflies
Half Day Tours
Full Day Tours
Transfers
Contact

Other pages will link to the other website - like on the other websites currently

```html
<!DOCTYPE html>
<html lang="en">
<head>
<meta charset="utf-8">
<title>Corvella Sky Tours – Home</title>
<link href="https://fonts.googleapis.com/css2?family=Hind:wght@500;600;700&family=Poppins:wght@400;500;600&display=swap" rel="stylesheet">
<style>
:root{
  --blue:#4a9fd5;
  --nav:#52a6dc;
  --green:#8dc63f;
  --orange:#c8582c;
  --orange-dark:#b14a22;
  --peach:#fdefe9;
  --ink:#222;
  --text:#555;
  --white:#fff;
}
*{box-sizing:border-box;margin:0;padding:0}
html,body{width:1200px;height:5025px;overflow:hidden}
body{font-family:"Poppins",sans-serif;color:var(--ink);background:var(--white);position:relative}
.abs{position:absolute}
.head{font-family:"Hind",sans-serif;font-weight:600}
.btn{position:absolute;display:flex;align-items:center;justify-content:center;gap:10px;border-radius:40px;color:var(--white);font-weight:500;text-transform:uppercase}
.btn svg{width:18px;height:18px}
.photo{position:absolute;overflow:hidden}

/* header */
.topbar{top:0;left:0;width:1200px;height:78px;background:var(--white)}
.brand{left:68px;top:18px;display:flex;align-items:center;gap:10px;font-size:22px;font-weight:600;color:var(--blue)}
.brand .mark{width:34px;height:34px;border-radius:50%;background:var(--blue)}
.contact-item{top:22px;display:flex;gap:12px;font-size:13px;line-height:18px}
.contact-item b{font-weight:600}
.book-top{left:973px;top:17px;width:160px;height:42px;background:var(--orange);font-size:16px}
.nav{top:78px;left:0;width:1200px;height:47px;background:var(--nav);display:flex;align-items:center;padding-left:70px;font-size:14px;color:var(--white)}
.nav a{color:var(--white);text-decoration:none;padding:0 26px;border-right:1px solid rgba(255,255,255,.6);line-height:14px}
.nav a:last-child{border:none}
.nav a.active{background:var(--green);line-height:47px;padding:0 32px;border:none;margin-right:0}

/* hero */
.hero{top:125px;left:0;width:1200px;height:747px;background:linear-gradient(180deg,#2f3b3f 0%,#6a6a55 30%,#a8783c 55%,#3f5f4f 100%)}
.hero .tag{left:68px;top:228px;font-size:27px;color:var(--green)}
.hero h1{left:68px;top:262px;font-size:68px;line-height:72px;color:var(--white)}
.hero p{left:68px;top:425px;width:580px;font-size:18px;line-height:30px;color:var(--white)}
.hero .btn{left:68px;top:543px;width:204px;height:62px;background:var(--green);font-size:19px}

/* about */
.about-img1{left:68px;top:982px;width:448px;height:373px;border-radius:26px;background:linear-gradient(135deg,#b06a3c,#7fbfc9 50%,#b9744a)}
.about-img2{left:302px;top:1158px;width:318px;height:289px;border-radius:26px;background:linear-gradient(180deg,#a9b9cc,#d9d2c4 45%,#4a4a48);border:2px solid var(--white)}
.sec-title{font-size:58px;color:var(--blue);display:flex;align-items:center;gap:14px}
.sec-title .rule{display:inline-block;width:95px;height:4px;background:var(--green);border-radius:2px}
.about h2{left:673px;top:975px}
.about h3{left:670px;top:1072px;width:470px;font-size:27px;line-height:37px;font-family:"Poppins",sans-serif;font-weight:600}
.body-copy{font-size:13.5px;line-height:27px;color:var(--text);text-align:justify}
.about .body-copy{left:670px;top:1170px;width:462px}
.orange-btn{background:var(--orange);font-size:14px}
.about .btn{left:673px;top:1365px;width:203px;height:50px}

/* scenic */
.scenic{top:1545px;left:0;width:1200px;height:623px;background:var(--peach)}
.scenic h2{left:105px;top:95px;font-size:58px;line-height:70px;color:var(--blue)}
.scenic .body-copy{left:105px;top:260px;width:462px}
.scenic .btn{left:107px;top:453px;width:203px;height:50px}
.video{left:618px;top:108px;width:476px;height:404px;border-radius:28px;background:linear-gradient(180deg,#3c4548,#8c9396 45%,#dfe2e3 70%,#9aa1a4)}
.play{left:197px;top:162px;width:82px;height:82px}

/* excursions */
.explore-title{top:2270px;left:0;width:1200px;justify-content:center}
.card{top:2398px;width:255px;height:380px;border-radius:18px}
.card .label{position:absolute;left:0;bottom:0;width:100%;height:75px;background:rgba(30,40,45,.55);color:var(--white);font-size:20px;display:flex;align-items:center;justify-content:center}

/* stats */
.stats{top:2878px;left:0;width:1200px;height:195px;background:var(--green)}
.stat{top:56px;display:flex;align-items:center;gap:14px;color:var(--white)}
.stat .ring{width:90px;height:90px;border:3px solid var(--white);border-radius:50%;display:flex;align-items:center;justify-content:center}
.stat .ring svg{width:44px;height:44px}
.stat b{display:block;font-family:"Hind",sans-serif;font-size:36px;line-height:36px;font-weight:600}
.stat span{font-size:17px;line-height:21px}

/* fly */
.fly{top:3073px;left:0;width:1200px;height:620px;background:linear-gradient(100deg,#222a2c 0%,#3b4a48 35%,#7c8e80 60%,#c2b79c 75%,#5b6a62 100%)}
.fly h2{left:68px;top:100px;font-size:68px;line-height:84px;color:var(--white)}
.fly h2 small{font-size:58px}
.fly .rule{left:68px;top:370px;width:95px;height:4px;background:var(--green)}
.fly .btn{top:432px;width:206px;height:62px;font-size:19px}

/* testimonials */
.testi-title{top:3790px;left:0;width:1200px;justify-content:center}
.arrow{width:42px;height:42px;border-radius:50%;display:flex;align-items:center;justify-content:center}
.arrow svg{width:20px;height:20px}
.arrow.outline{border:2px solid var(--green)}
.arrow.solid{background:var(--green)}
.quote{left:165px;top:3925px;width:180px;height:150px}
.testi-text{left:358px;top:3942px;width:674px;font-size:14.5px;line-height:27px;color:var(--text);text-align:justify}
.testi-text .last{display:block;text-align:center}
.avatar{left:482px;top:4132px;width:50px;height:50px;border-radius:50%;background:linear-gradient(#c9c9c9,#8f8f8f)}
.author{left:552px;top:4135px}
.author b{display:block;font-size:21px;color:var(--orange);font-weight:500}
.author span{font-size:11px;color:var(--text)}

/* gallery */
.gal{top:4280px;height:328px}

/* footer */
.footer{top:4608px;left:0;width:1200px;height:362px;background:var(--orange);color:var(--white)}
.footer .brand{left:68px;top:72px;color:var(--white);font-size:30px}
.footer .brand .mark{background:var(--white);width:40px;height:40px}
.footer .about-text{left:68px;top:165px;width:310px;font-size:13px;line-height:22px}
.footer h4{font-size:17px;font-weight:500}
.links{left:415px;top:72px}
.links ul{list-style:none;margin-top:30px}
.links li{font-size:13px;line-height:26px;display:flex;align-items:center;gap:10px}
.links li::before{content:"";width:8px;height:8px;border-radius:50%;background:var(--nav)}
.fcontact{left:621px;top:72px}
.fc-row{display:flex;gap:16px;font-size:12.5px;line-height:16px;margin-top:28px}
.fc-row .ic{width:28px;height:28px;border-radius:6px;background:var(--nav);display:flex;align-items:center;justify-content:center;flex:none}
.fc-row .ic svg{width:16px;height:16px}
.news{left:917px;top:72px;width:200px}
.news p{font-size:13px;line-height:17px;margin-top:28px}
.news .field{width:195px;height:29px;background:var(--white);margin-top:12px}
.news .sub{width:98px;height:27px;margin-top:12px;border-radius:20px;background:var(--nav);font-size:10px;display:flex;align-items:center;justify-content:center}
.bottom{top:4970px;left:0;width:1200px;height:55px;background:var(--orange-dark);color:var(--white);font-size:11.5px}
.flags{left:570px;top:16px;display:flex;gap:13px}
.flags i{display:block;width:34px;height:24px}
.social{left:1013px;top:14px;display:flex;gap:6px}
.social i{display:block;width:26px;height:26px;border-radius:50%;background:var(--nav)}
</style>
</head>
<body>

<header>
  <div class="abs topbar">
    <div class="abs brand"><span class="mark"></span>Corvella Sky Tours</div>
    <div class="abs contact-item" style="left:520px">
      <svg width="24" height="24" viewBox="0 0 24 24" fill="none" stroke="#c8582c" stroke-width="2"><path d="M5 3h4l2 5-3 2a11 11 0 0 0 6 6l2-3 5 2v4a2 2 0 0 1-2 2A17 17 0 0 1 3 5a2 2 0 0 1 2-2z"/></svg>
      <div><b>Call:</b><br>08 9100 4417</div>
    </div>
    <div class="abs contact-item" style="left:707px">
      <svg width="24" height="24" viewBox="0 0 24 24" fill="#c8582c"><path d="M2 5h20v14H2z"/><path d="M2 5l10 8 10-8" stroke="#fff" stroke-width="1.6" fill="none"/></svg>
      <div><b>Email:</b><br>info@brightvalewings.com.au</div>
    </div>
    <div class="btn book-top">Book Now</div>
  </div>
  <nav class="abs nav">
    <a class="active">Home</a><a>About Us</a><a>Gallery</a><a>News/Blog</a><a>Overflies</a><a>Half Day Tours</a><a>Full Day Tours</a><a>Transfers</a><a>Contact</a>
  </nav>
</header>

<section class="abs hero" role="img" aria-label="Aerial photograph of the bay at sunset with golden tidal flats and winding blue channels">
  <div class="abs tag head">Relax &amp; Enjoy</div>
  <h1 class="abs head">Discover Corvella Bay<br>Scenic Flights</h1>
  <p class="abs">Lorem ipsum dolor sit amet, consectetur adipi scing elit. Vi vamus finibus enim nec odio ultricies dictum. Donec vel nisl posuere, finibus ex vel.</p>
  <div class="btn">Learn More <svg viewBox="0 0 24 24" fill="none" stroke="#fff" stroke-width="2"><circle cx="12" cy="12" r="9"/><path d="M8 12h8M13 9l3 3-3 3"/></svg></div>
</section>

<section class="about">
  <div class="photo about-img1" role="img" aria-label="View from under an aircraft wing over red desert and turquoise lagoon"></div>
  <div class="photo about-img2" role="img" aria-label="Small aircraft parked at an airfield at dusk"></div>
  <h2 class="abs head sec-title">About Us <span class="rule"></span></h2>
  <h3 class="abs">Corvella Wings flight crew are trained to the highest standard.</h3>
  <p class="abs body-copy">Our commitment to safety and service make us one of the highly regarded charter services in WA. Donec vel nisl posuere, fini bus ex vel, dictum mauris. Praesent nec tempus elit. Morbi quis est euis mod, mollis diam vel, gravida magna. Nullam malesuada est dapibus nisi convallis ornare. Pel lentesque gravida augue at metus accumsan varius. Praesent nec digni ssim erat.</p>
  <div class="btn orange-btn">Discover More <svg viewBox="0 0 24 24" fill="none" stroke="#fff" stroke-width="2"><circle cx="12" cy="12" r="9"/><path d="M8 12h8M13 9l3 3-3 3"/></svg></div>
</section>

<section class="abs scenic">
  <h2 class="abs head">Scenic Flights<br>and Charter <span style="display:inline-block;width:95px;height:4px;background:var(--green);vertical-align:middle;margin-left:6px"></span></h2>
  <p class="abs body-copy">Lorem ipsum dolor sit amet, consectetur adipiscing elit. Vivamus finibus enim nec odio ultricies dictum. Donec vel nisl posuere, fini bus ex vel, dictum mauris. Praesent nec tempus elit. Morbi quis est euismod, mollis diam vel, gravida magna. Nullam malesuada est dapibus nisi convallis ornare. Pel lentesque gravida augue at metus accumsan varius. Praesent nec digni ssim erat.</p>
  <div class="btn orange-btn">Discover More <svg viewBox="0 0 24 24" fill="none" stroke="#fff" stroke-width="2"><circle cx="12" cy="12" r="9"/><path d="M8 12h8M13 9l3 3-3 3"/></svg></div>
  <div class="photo video" role="img" aria-label="Video still: aircraft wing above the clouds">
    <svg class="abs play" viewBox="0 0 82 82"><circle cx="41" cy="41" r="38" fill="none" stroke="#fff" stroke-width="4"/><path d="M32 25l26 16-26 16z" fill="#fff"/></svg>
  </div>
</section>

<section>
  <h2 class="abs head sec-title explore-title"><span class="rule"></span>Explore Our Excursions<span class="rule"></span></h2>
  <div class="photo card" style="left:68px;background:linear-gradient(180deg,#1f4fa0,#5a86c4 40%,#d8d8d8 60%,#3a3a3a)" role="img" aria-label="Pilot beside an aircraft wing under blue sky"><div class="label">Overflies</div></div>
  <div class="photo card" style="left:338px;background:linear-gradient(160deg,#1aa5b8,#5ed0d6 50%,#d9c7a0 70%,#2a9fb0)" role="img" aria-label="Aerial view of turquoise water and a sandy spit"><div class="label">Half Day Tours</div></div>
  <div class="photo card" style="left:608px;background:linear-gradient(180deg,#3e7fc8,#8fbfe6 45%,#e6d2b0 75%,#c9a77c)" role="img" aria-label="Family playing on a sunny beach"><div class="label">Full Day Tours</div></div>
  <div class="photo card" style="left:878px;background:linear-gradient(180deg,#7fc6d9,#3fb0c0 45%,#2d7f88 80%,#1f5c62)" role="img" aria-label="Aircraft wing over tropical islands"><div class="label">Custom Tours</div></div>
</section>

<section class="abs stats">
  <div class="abs stat" style="left:68px">
    <div class="ring"><svg viewBox="0 0 24 24" fill="#fff"><path d="M2 14l2-1 4 1 4-3-5-5 2-1 7 4 4-2c1 0 1.5.8.8 1.3L8 16H4z"/></svg></div>
    <div><b>13+</b><span>Scenic Fights &amp;<br>Charters</span></div>
  </div>
  <div class="abs stat" style="left:345px">
    <div class="ring"><svg viewBox="0 0 24 24" fill="none" stroke="#fff" stroke-width="2"><path d="M12 22s7-7 7-12a7 7 0 0 0-14 0c0 5 7 12 7 12z"/><circle cx="12" cy="10" r="2.5"/></svg></div>
    <div><b>6+</b><span>Destinations</span></div>
  </div>
  <div class="abs stat" style="left:603px">
    <div class="ring"><svg viewBox="0 0 24 24" fill="none" stroke="#fff" stroke-width="2"><circle cx="7" cy="6" r="2.5"/><path d="M7 9v3M7 14c0 4 10 0 10 5M15 13v6M15 13l4 2-4 2"/></svg></div>
    <div><b>10,000+</b><span>Scenic Trips</span></div>
  </div>
  <div class="abs stat" style="left:873px">
    <div class="ring"><svg viewBox="0 0 24 24" fill="#fff"><circle cx="12" cy="8" r="3"/><circle cx="5" cy="10" r="2.2"/><circle cx="19" cy="10" r="2.2"/><path d="M6 19a6 6 0 0 1 12 0zM1 18a4 4 0 0 1 5-3.5L5 18zM23 18a4 4 0 0 0-5-3.5l1 3.5z"/></svg></div>
    <div><b>50,000+</b><span>Happy Customers</span></div>
  </div>
</section>

<section class="abs fly" role="img" aria-label="Aerial view through an aircraft window of a long coastal peninsula and shallow turquoise water">
  <h2 class="abs head">Fly with Us and<br>Discover the<br><small>Beauty of Corvella Bay</small></h2>
  <div class="abs rule"></div>
  <div class="btn" style="left:68px;background:var(--nav)">Contact Us <svg viewBox="0 0 24 24" fill="none" stroke="#fff" stroke-width="2"><circle cx="12" cy="12" r="9"/><path d="M8 12h8M13 9l3 3-3 3"/></svg></div>
  <div class="btn" style="left:288px;background:var(--green)">Book Now <svg viewBox="0 0 24 24" fill="none" stroke="#fff" stroke-width="2"><circle cx="12" cy="12" r="9"/><path d="M8 12h8M13 9l3 3-3 3"/></svg></div>
</section>

<section>
  <h2 class="abs head sec-title testi-title"><span class="rule"></span>What Customer Say About Us<span class="rule"></span></h2>
  <div class="abs arrow outline" style="left:68px;top:4026px"><svg viewBox="0 0 24 24" fill="none" stroke="#8dc63f" stroke-width="2.5"><path d="M19 12H5M11 6l-6 6 6 6"/></svg></div>
  <div class="abs arrow solid" style="left:1090px;top:4026px"><svg viewBox="0 0 24 24" fill="none" stroke="#fff" stroke-width="2.5"><path d="M5 12h14M13 6l6 6-6 6"/></svg></div>
  <svg class="abs quote" viewBox="0 0 180 150" fill="#c8582c"><path d="M0 75C0 30 20 5 70 0v25c-22 5-30 18-30 40h30v85H0zM105 75c0-45 20-70 70-75v25c-22 5-30 18-30 40h30v85h-70z"/></svg>
  <p class="abs testi-text">Lorem ipsum dolor sit amet, conse ctetuer adipiscing elit. Aenean comodo ligula eget dolor. Aenean massa. Cum sociis natoque pen atibus et magnis dis parturient montes, nascetur ridiculus mus. Donec quam felis, ultricies nec, pellentesque eu, pretium quis, sem. Nulla consequat massa quis enim. Donec pede justo, fringilla vel, aliquet nec, vulputate eget, arcu. In enim justo, rhoncus ut, imperdiet a, venenatis vitae, justo. Nullam dictum felis eu pede mollis pretium. Integer tincidunt. <span class="last">Cras dapibus. Vivamus elementum</span></p>
  <div class="abs avatar" role="img" aria-label="Customer portrait"></div>
  <div class="abs author"><b>Dorian Vale</b><span>Managing Director</span></div>
</section>

<section>
  <div class="photo gal" style="left:0;width:285px;background:linear-gradient(180deg,#8fa6c2,#c7ced6 45%,#3a3f48)" role="img" aria-label="Pilot standing beside an aircraft"></div>
  <div class="photo gal" style="left:300px;width:292px;background:linear-gradient(180deg,#c9b3a0,#9a6a55 40%,#4fb3bd 75%,#2a8f9c)" role="img" aria-label="Aerial view of red cliffs and blue water"></div>
  <div class="photo gal" style="left:607px;width:291px;background:linear-gradient(150deg,#1a9ec2,#6fd3da 50%,#e6dcc0 65%,#2aa9c0)" role="img" aria-label="Aerial view of sandbars in turquoise sea"></div>
  <div class="photo gal" style="left:912px;width:288px;background:linear-gradient(180deg,#8e969c,#b7bbbe 45%,#6e6a62)" role="img" aria-label="Group of visitors at an airfield"></div>
  <div class="abs arrow solid" style="left:48px;top:4423px;background:var(--white)"><svg viewBox="0 0 24 24" fill="none" stroke="#8dc63f" stroke-width="2.5"><path d="M19 12H5M11 6l-6 6 6 6"/></svg></div>
  <div class="abs arrow solid" style="left:1110px;top:4423px"><svg viewBox="0 0 24 24" fill="none" stroke="#fff" stroke-width="2.5"><path d="M5 12h14M13 6l6 6-6 6"/></svg></div>
</section>

<footer class="abs footer">
  <div class="abs brand"><span class="mark"></span>Corvella Sky Tours</div>
  <p class="abs about-text">Corvella Wings flight crew are trained to the highest standard. Our commitment to safety and service make us one of the highly regarded charter services in WA.</p>
  <div class="abs links">
    <h4>Quick Links</h4>
    <ul><li>About Us</li><li>Gallery</li><li>News/Blog</li><li>Overflies</li><li>Half Day Tours</li><li>Full Day Tours</li><li>Transfers</li><li>Contact</li></ul>
  </div>
  <div class="abs fcontact">
    <h4>Contact Us</h4>
    <div class="fc-row"><span class="ic"><svg viewBox="0 0 24 24" fill="#fff"><path d="M5 3h4l2 5-3 2a11 11 0 0 0 6 6l2-3 5 2v4a2 2 0 0 1-2 2A17 17 0 0 1 3 5a2 2 0 0 1 2-2z"/></svg></span><div>CALL US<br>08 9100 4417</div></div>
    <div class="fc-row"><span class="ic"><svg viewBox="0 0 24 24" fill="#fff"><path d="M2 5h20v14H2z"/></svg></span><div>EMAIL US<br>info@brightvalewings.com.au</div></div>
    <div class="fc-row"><span class="ic"><svg viewBox="0 0 24 24" fill="#fff"><path d="M12 22s7-7 7-12a7 7 0 0 0-14 0c0 5 7 12 7 12z"/></svg></span><div>Corvella Airstrip Rd<br>Halden, WA, 6500<br>Australia</div></div>
  </div>
  <div class="abs news">
    <h4>Our Newsletter</h4>
    <p>Subscribe our newsletter to get the latest news.</p>
    <div class="field"></div>
    <div class="sub">SUBSCRIBE</div>
  </div>
</footer>
<div class="abs bottom">
  <div class="abs" style="left:68px;top:20px">Copyright © 2025 All Rights Reserved By Company Name</div>
  <div class="abs flags"><i style="background:linear-gradient(#000 33%,#d00 33% 66%,#fc0 66%)"></i><i style="background:#1f3a8a"></i><i style="background:#fff"></i><i style="background:#d52b1e"></i></div>
  <div class="abs social"><i></i><i></i><i></i><i></i></div>
</div>

</body>
</html>
```